BLUE HAVEN (Business Card for Training Company)

Blue Haven is a training and consultancy company with a focus on executive protection and medical. I would like the card to be nice and sharp, not overdone and in black and red. I would also like it to highlight that it is "A Dravin Company"

I would like it to be simple and highlight a few things.

1. Name
2. Title
3. Phone Number
4. Email

I would also like www.dravinholdings.example/blue-haven to be on the card somewhere.

Target Market(s)

Security Companies

Industry/Entity Type

Security

Contact Information for Business Card

Blue Haven is a training and consultancy company with a focus on executive protection and medical. I would like the card to be nice and sharp, not overdone and in black and red. I would also like it to highlight that it is "A Dravin Company" I would like it to be simple and highlight a few things. 1. Name 2. Title 3. Phone Number 4. Email I would also like www.dravinholdings.example/blue-haven to be on the card somewhere.

Requirements
Must have
• A Dravin Company listed on the card and the website
Nice to have
• Highlight Medical Training, Consultancy & Executive Protection Courses

```html
<!DOCTYPE html>
<html lang="en">
<head>
<meta charset="utf-8">
<title>Blue Haven – Business Card</title>
<link rel="stylesheet" href="https://fonts.googleapis.com/css2?family=Roboto:wght@300;400;500;700;900&display=swap">
<style>
  :root {
    --stage: #f2efef;
    --crimson: #630c10;
    --crimson-deep: #461410;
    --edge-dark: #3c0e0f;
    --ink: #111111;
    --paper: #ffffff;
  }
  * { box-sizing: border-box; margin: 0; padding: 0; }
  html, body {
    width: 1200px; height: 1200px; overflow: hidden;
    background: var(--stage);
    font-family: "Roboto", Arial, sans-serif;
  }
  .stage { position: relative; width: 1200px; height: 1200px; }

  .card { position: absolute; width: 631px; overflow: hidden; }

  /* Front */
  .card-front {
    left: 286px; top: 176px; height: 376px;
    background: var(--crimson);
  }
  .front-name {
    position: absolute; left: 0; right: 0; top: 143px;
    text-align: center; color: var(--paper);
    font-weight: 900; font-size: 34px; line-height: 33px; letter-spacing: 1px;
  }
  .web-band {
    position: absolute; left: 0; right: 0; top: 283px; height: 60px;
    background: var(--crimson-deep);
    display: flex; align-items: center; justify-content: center; gap: 9px;
    color: var(--paper); font-weight: 300; font-size: 17px;
  }
  .web-band svg { width: 22px; height: 22px; }

  /* Back */
  .card-back {
    left: 284px; top: 602px; height: 379px;
    background: var(--paper);
  }
  .back-art { position: absolute; inset: 0; width: 100%; height: 100%; }
  .brand-name {
    position: absolute; left: 55px; top: 84px;
    color: var(--ink); font-weight: 900; font-size: 34px; line-height: 33px; letter-spacing: 1px;
  }
  .parent-line {
    position: absolute; left: 55px; top: 157px;
    color: var(--ink); font-weight: 700; font-size: 25px;
  }
  .person {
    position: absolute; right: 55px; top: 50px; text-align: right; color: var(--ink);
  }
  .person-name { font-weight: 700; font-size: 27px; line-height: 32px; }
  .person-title { font-weight: 300; font-size: 19px; line-height: 22px; }
  .contacts {
    position: absolute; left: 392px; top: 232px; list-style: none;
    color: var(--paper); font-size: 16px; font-weight: 400;
  }
  .contacts li { display: flex; align-items: flex-start; gap: 8px; line-height: 20px; margin-bottom: 6px; }
  .contacts svg { width: 12px; height: 14px; margin-top: 3px; flex: none; }
</style>
</head>
<body>
<main class="stage">

  <section class="card card-front" aria-label="Card front">
    <div class="front-name">BLUE<br>HAVEN</div>
    <div class="web-band">
      <svg viewBox="0 0 24 24" fill="none" stroke="#fff" stroke-width="1.4" aria-hidden="true">
        <circle cx="12" cy="12" r="10"/>
        <ellipse cx="12" cy="12" rx="4.5" ry="10"/>
        <line x1="2" y1="12" x2="22" y2="12"/>
        <path d="M4 6.5h16M4 17.5h16"/>
      </svg>
      <span>www.dravinholdings.example/blue-haven</span>
    </div>
  </section>

  <section class="card card-back" aria-label="Card back">
    <svg class="back-art" viewBox="0 0 1016 610" preserveAspectRatio="none" aria-hidden="true">
      <path d="M0 0 H305 C200 52 110 100 0 113 Z" fill="var(--edge-dark)"/>
      <path d="M0 0 H265 C180 45 90 78 0 88 Z" fill="var(--crimson)"/>
      <path d="M0 610 L0 602 C300 440 600 300 760 275 C880 255 980 300 1016 345 V610 Z" fill="var(--edge-dark)"/>
      <path d="M0 610 C300 455 600 325 760 300 C880 285 975 315 1016 385 V610 Z" fill="var(--crimson)"/>
      <path d="M0 608 C300 452 600 322 760 297 C880 282 975 312 1016 380" fill="none" stroke="#9a8e8e" stroke-width="2"/>
    </svg>

    <div class="brand-name">BLUE<br>HAVEN</div>
    <div class="parent-line">A Dravin Company</div>

    <div class="person">
      <div class="person-name">JHONE DOE</div>
      <div class="person-title">Operation Manager</div>
    </div>

    <ul class="contacts">
      <li>
        <svg viewBox="0 0 12 16" fill="none" stroke="#fff" stroke-width="1" aria-hidden="true"><rect x="1.5" y="0.5" width="9" height="15" rx="1.5"/><line x1="1.5" y1="13" x2="10.5" y2="13"/></svg>
        <span>+00 123 123 123</span>
      </li>
      <li>
        <svg viewBox="0 0 14 14" fill="none" stroke="#fff" stroke-width="1" aria-hidden="true"><path d="M1 5 L7 1 L13 5 V13 H1 Z"/><path d="M1 5 L7 9.5 L13 5"/></svg>
        <span>name@company.com</span>
      </li>
      <li>
        <svg viewBox="0 0 12 16" fill="none" stroke="#fff" stroke-width="1.2" aria-hidden="true"><path d="M6 15 C2 10 1 8 1 6 A5 5 0 0 1 11 6 C11 8 10 10 6 15 Z"/><circle cx="6" cy="6" r="2"/></svg>
        <span>07, address goes here,<br>city name here - 1234</span>
      </li>
    </ul>
  </section>

</main>
</body>
</html>
```